Lounge Bar Menu

We need an elegant Bar Menu for ou Lounge Bar.
Logo attached.
We already have the support. A cover like a book in A5 format.
Attached as well our menu.

Industry/Entity Type

Bar, Hotel4*

```html
<!DOCTYPE html>
<html lang="fr">
<head>
<meta charset="UTF-8">
<title>Solenne Lounge-Bar — Menu</title>
<link href="https://fonts.googleapis.com/css2?family=Montserrat:wght@700;800&display=swap" rel="stylesheet">
<style>
  :root {
    --ink: #121212;
    --paper-light: #f1f2f8;
    --paper-mid: #e6e8f2;
    --paper-vein: #dcdfea;
    --plate: #111111;
    --plate-text: #ffffff;
  }
  html, body {
    margin: 0;
    padding: 0;
    overflow: hidden;
  }
  .menu-card {
    position: relative;
    width: 848px;
    height: 1200px;
    overflow: hidden;
    font-family: "Montserrat", Arial, sans-serif;
    color: var(--ink);
    background: var(--paper-light);
  }
  .marble-texture {
    position: absolute;
    inset: 0;
    background:
      radial-gradient(ellipse at 20% 15%, var(--paper-light) 0%, transparent 60%),
      radial-gradient(ellipse at 80% 70%, var(--paper-vein) 0%, transparent 55%),
      linear-gradient(160deg, var(--paper-light) 0%, var(--paper-mid) 50%, var(--paper-light) 100%);
  }
  .title-plate {
    position: absolute;
    left: 275px;
    top: 0;
    width: 298px;
    height: 133px;
    background: var(--plate);
    display: flex;
    align-items: center;
    justify-content: center;
  }
  .title-plate h1 {
    margin: 0;
    color: var(--plate-text);
    font-weight: 800;
    font-size: 80px;
    letter-spacing: 1px;
    line-height: 1;
    padding-top: 4px;
  }
  .menu-body {
    position: absolute;
    left: 0;
    top: 253px;
    width: 848px;
    text-align: center;
    font-weight: 700;
    font-size: 18.6px;
    line-height: 31.2px;
    white-space: nowrap;
  }
  .menu-body p {
    margin: 0;
  }
  .menu-section {
    margin-bottom: 31.2px;
  }
  .footnote {
    white-space: normal;
    padding: 0 8px;
  }
  .brand-name {
    position: absolute;
    left: 248px;
    top: 1000px;
    width: 384px;
    height: 200px;
    display: flex;
    align-items: center;
    justify-content: center;
    font-weight: 700;
    font-size: 30px;
    letter-spacing: 6px;
    color: var(--ink);
  }
</style>
</head>
<body>
  <div class="menu-card">
    <div class="marble-texture" role="img" aria-label="Soft white marble texture background"></div>

    <header class="title-plate">
      <h1>MENU</h1>
    </header>

    <main class="menu-body">
      <section class="menu-section">
        <p class="section-title">----------------------- A PARTAGER OU PAS -------------------------</p>
        <p class="section-label">Room:</p>
        <p>• Croque Miura jambon truffé &amp; Reblochon - 14 € (19e)</p>
        <p>• Légumes crus, Houmous &amp; Cervelle de Canus - 7 € (12e)</p>
        <p>• Rillettes de Sardines au beurre salé &amp; citron vert - 7 € (12e)</p>
        <p>• Planche de Charcuterie de Savoie - 9 € (grande 14 €) (14e et 19e)</p>
        <p>• Mozzarella di buffala &amp; tomates cerise - 11 € (16e)</p>
        <p>• Truite Gravlax, pain toasté &amp; Crème crue - 14 € (19e)</p>
      </section>

      <section class="menu-section">
        <p class="section-title">----------------------- FROMAGES -----------------------</p>
        <p class="section-label">Fromages:</p>
        <p>• Fromages de notre région, mesclun à l'huile de noisette - 12 € (17e)</p>
        <p>• Faisselle sucre ou salé - 7 € (9e)</p>
      </section>

      <section class="menu-section">
        <p class="section-title">----------------------- DESSERTS -----------------------</p>
        <p class="section-label">Desserts:</p>
        <p>• Tarte du jour - 9 € (12e)</p>
        <p>• Salade de fruits frais et financier - 7 € (11e)</p>
        <p>• Panna Cotta coulis de fruits - 7 € (11e)</p>
      </section>

      <p class="footnote">Please note that the prices are indicated in euros (€) and the numbers in parentheses represent the prices for a larger portion (if applicable). Enjoy your meal!</p>
    </main>

    <footer class="brand-name">SOLENNE LOUNGE-BAR</footer>
  </div>
</body>
</html>
```